quorvadeal.com redesign with wireframes, white space and custom form are very important

Need a new two column design that will convert easily to mobile responsive. Lots of white space. Winning design will probably be based on header area and making the custom form stand out. I want the header to be very much like www.talbekmo.com except the form not to go up into the header.
Here are some of the websites I really like:
www.pivrostacks.com
http://glendarokfastmove.com/
http://morquilandestate.com/

We buy homes for cash and close fast. Our target is a home seller who is desperate to sell quickly.
I have uploaded my really ugly wireframe and my logo. I also uploaded my photo for the about us box and a possible photo to use for the header.
The copy on the wireframe is what I will be using except for the about us box.

Here is the exact link for video to frame in the top left box.
https://example-vidhost.net/Kp39xqTzR2a

Number of Pages Required

1 page

Font styles to use
Sans Serif

Colors
0592cd
85cae6
eaf1f7
fbee3d
ec1f27

Requirements
Must have
• Everything on wireframe.
• Must use Verdana font and nothing should be smaller than 12 point. Most should be in 14 point. (except maybe inside of form)

```html
<!DOCTYPE html>
<html lang="en">
<head>
<meta charset="utf-8">
<title>quorvadeal.com — Sell Your Home For Cash In 8 Days</title>
<link href="https://fonts.googleapis.com/css2?family=Open+Sans:wght@400;600;700&display=swap" rel="stylesheet">
<style>
:root{
  --blue:#0592cd;
  --sky:#85cae6;
  --mist:#eaf1f7;
  --yellow:#fbee3d;
  --red:#ec1f27;
  --ink:#333;
  --muted:#666;
  --line:#dde3e8;
  --dark:#2b2b2b;
  --white:#fff;
}
*{box-sizing:border-box;margin:0;padding:0}
html,body{width:1200px;height:2672px;overflow:hidden}
body{font-family:Verdana,"Open Sans",sans-serif;color:var(--ink);font-size:14px;line-height:1.5;background:var(--white)}
.wrap{width:1080px;margin:0 auto;position:relative}
section,header,footer,nav.links{overflow:hidden}

/* header */
.site-header{height:90px;background:var(--white);border-bottom:1px solid var(--line)}
.site-header .wrap{display:flex;align-items:center;height:90px}
.brand{display:flex;align-items:center;gap:10px;font-size:22px;font-weight:700;color:var(--red);width:230px}
.brand .mark{width:22px;height:22px;background:var(--red);flex:none}
.nav{display:flex;gap:34px;margin-left:20px}
.nav a{color:var(--ink);text-decoration:none;font-size:14px}
.nav a.active{color:var(--blue)}
.phone{margin-left:auto;text-align:right;color:var(--red)}
.phone small{display:block;font-size:12px;color:var(--muted)}
.phone strong{font-size:22px;display:flex;align-items:center;gap:8px}

/* hero */
.hero{height:470px;background:linear-gradient(180deg,#3f7fbf 0%,#7fb2dd 35%,#c9d6e0 55%,#6f8f5a 75%,#4d6a3c 100%);position:relative;text-align:center;color:var(--white)}
.hero .title{position:absolute;top:80px;left:0;right:0;text-shadow:0 2px 4px rgba(0,0,0,.4)}
.hero h1{font-size:34px;font-weight:700}
.hero p{font-size:22px}
.hero .arrow{position:absolute;top:222px;width:26px;height:26px;border-radius:50%;background:rgba(255,255,255,.5)}

/* main */
.main{height:600px;padding-top:40px}
.main .wrap{display:flex;justify-content:space-between}
.benefits{width:560px;padding-top:70px}
.benefits h2{color:var(--red);font-size:20px;font-weight:700;margin-bottom:14px}
.ticks{list-style:none}
.ticks li{display:flex;align-items:center;gap:10px;margin-bottom:6px}
.video-intro{margin:18px 0 10px}
.video{width:560px;height:300px;background:linear-gradient(160deg,#c6ccd4,#7c8898);position:relative}
.video .bar{position:absolute;left:0;right:0;bottom:0;height:30px;background:rgba(0,0,0,.7)}
.video .play{position:absolute;left:250px;top:115px;width:60px;height:60px;border-radius:50%;background:rgba(0,0,0,.6)}

.lead-form{width:480px;background:var(--yellow);padding:0 0 30px}
.lead-form header{background:var(--red);color:var(--white);text-align:center;padding:18px 20px}
.lead-form header h3{font-size:20px}
.lead-form header p{font-size:12px}
.lead-form form{padding:24px 30px 0;display:flex;flex-direction:column;gap:10px}
.lead-form .field{background:var(--white);border:1px solid #d9c92a;height:34px;padding:0 12px;font-size:12px;color:#888;display:flex;align-items:center}
.lead-form .submit{margin-top:16px;background:var(--red);color:var(--white);text-align:center;font-size:15px;font-weight:700;padding:14px}

/* band */
.band{height:20px;background:var(--mist)}

/* about section */
.info{height:440px;padding-top:40px}
.info .wrap{display:flex;justify-content:space-between}
.intro{width:540px}
.intro .big{font-size:17px;margin-bottom:12px}
.intro p{font-size:12px;color:var(--muted);margin-bottom:12px}
.intro h4{font-size:15px;margin-bottom:8px}
.intro ul{list-style:none}
.intro li{display:flex;gap:10px;align-items:center;font-size:13px;margin-bottom:4px}
.sidebar{width:480px}
.privacy{display:flex;justify-content:space-between;align-items:center;border-bottom:1px solid var(--line);padding-bottom:10px}
.privacy h5{font-size:13px}
.socials{display:flex;gap:8px}
.socials span{width:30px;height:30px;background:var(--blue);display:block}
.call-bar{background:var(--mist);text-align:center;padding:10px;font-size:13px;margin:14px 0}
.testimonial{border:1px solid var(--line);padding:14px 18px}
.testimonial h5{color:var(--red);font-size:16px;border-bottom:1px solid var(--line);padding-bottom:6px;margin-bottom:8px}
.testimonial p{font-size:12px;color:var(--muted)}
.testimonial .by{display:flex;justify-content:space-between;font-size:12px;color:var(--blue);margin-top:6px}
.about{display:flex;gap:18px;margin-top:18px}
.about .photo{width:150px;height:130px;flex:none;background:linear-gradient(#9aa7b5,#5d6a78)}
.about h5{font-size:20px;border-bottom:1px solid var(--line);margin-bottom:6px}
.about p{font-size:12px;color:var(--muted)}

/* posts and cities */
.lower{height:720px;padding-top:40px;background:var(--white)}
.lower .wrap{display:flex;justify-content:space-between}
.posts{width:540px}
.post{display:flex;gap:20px;margin-bottom:30px}
.post .thumb{width:180px;height:180px;flex:none}
.post h6{font-size:13px;margin-bottom:6px}
.post p{font-size:12px;color:var(--muted)}
.post .meta{font-size:12px;color:var(--blue);margin-top:8px;text-align:right}
.cities{width:500px}
.cities h4{font-size:15px;margin-bottom:10px}
.cities p{font-size:12px;color:var(--muted);margin-bottom:10px}
.cities .pic{height:300px;background:linear-gradient(180deg,#6fa4d8,#b6cfe6 40%,#7e9467 80%);margin:10px 0 14px}
.cities .caption{font-size:16px}

.links{height:60px;border-top:1px solid var(--line)}
.links .wrap{display:grid;grid-template-columns:repeat(3,180px);gap:4px 0;padding-top:10px;font-size:12px}

/* footer */
.site-footer{height:200px;background:var(--mist);border-top:4px solid var(--blue)}
.site-footer .wrap{display:flex;padding-top:30px;gap:60px}
.site-footer .brand{width:260px}
.fcol h6{font-size:16px;margin-bottom:8px}
.fcol p,.fcol li{font-size:12px;color:var(--muted);list-style:none}
.fcol{width:230px}
.bottom{height:72px;background:var(--dark);color:#bbb;font-size:12px}
.bottom .wrap{line-height:72px}
</style>
</head>
<body>

<header class="site-header">
  <div class="wrap">
    <div class="brand"><span class="mark"></span>quorvadeal.com</div>
    <nav class="nav">
      <a class="active" href="#">Sell Your Home</a>
      <a href="#">How it works</a>
      <a href="#">Stop Foreclosure</a>
      <a href="#">Probate</a>
      <a href="#">Contact</a>
    </nav>
    <div class="phone">
      <small>Nights and weekends ok</small>
      <strong>
        <svg width="20" height="20" viewBox="0 0 24 24"><path fill="#ec1f27" d="M6.6 10.8a15 15 0 0 0 6.6 6.6l2.2-2.2c.3-.3.7-.4 1-.2 1.1.4 2.3.6 3.6.6.6 0 1 .4 1 1V20c0 .6-.4 1-1 1A17 17 0 0 1 3 4c0-.6.4-1 1-1h3.5c.6 0 1 .4 1 1 0 1.3.2 2.5.6 3.6.1.3 0 .7-.2 1z"/></svg>
        407 · 555 · 0186
      </strong>
    </div>
  </div>
</header>

<section class="hero" role="img" aria-label="Photo of a single-storey white house with trees under a blue sky">
  <span class="arrow" style="left:20px"></span>
  <span class="arrow" style="right:20px"></span>
  <div class="title">
    <h1>Sell Your Home For Cash In 8 Days</h1>
    <p>We buy Houses Nationwide.</p>
  </div>
</section>

<section class="main">
  <div class="wrap">
    <div class="benefits">
      <h2>These Are The Benefits Of Selling Your Home To Us.</h2>
      <ul class="ticks">
        <li><svg width="14" height="14" viewBox="0 0 14 14"><path d="M2 7l3 3 7-7" stroke="#ec1f27" stroke-width="2.2" fill="none"/></svg>You pick the closing date</li>
        <li><svg width="14" height="14" viewBox="0 0 14 14"><path d="M2 7l3 3 7-7" stroke="#ec1f27" stroke-width="2.2" fill="none"/></svg>You pay NO commissions or fees</li>
        <li><svg width="14" height="14" viewBox="0 0 14 14"><path d="M2 7l3 3 7-7" stroke="#ec1f27" stroke-width="2.2" fill="none"/></svg>You don't have to paint, clean or make repairs</li>
      </ul>
      <p class="video-intro">Watch To See Our President Arlen Explain How Easy It Is To Sell To Us.</p>
      <div class="video" role="img" aria-label="Embedded video of the company president explaining the selling process">
        <span class="play"></span><span class="bar"></span>
      </div>
    </div>

    <aside class="lead-form">
      <header>
        <h3>Yes, I Want To Sell My Home Fast!</h3>
        <p>Get a no-obligation written offer in 48 hours</p>
      </header>
      <form>
        <div class="field">Your Name</div>
        <div class="field">Your phone number</div>
        <div class="field">Your Email Address</div>
        <div class="field">Property Address including City, State and Zip Code</div>
        <div class="field">Reason needed</div>
        <div class="field">Reason needed if any</div>
        <div class="field">Asking price</div>
        <div class="field">Comments</div>
        <div class="submit">Submit, To Get Started Selling Your Home Fast</div>
      </form>
    </aside>
  </div>
</section>

<div class="band"></div>

<section class="info">
  <div class="wrap">
    <div class="intro">
      <p class="big">Sell your home or house fast for cash to a professional investor company. We buy houses and close quickly.</p>
      <p>Selling a home on your own can leave loose ends. From timelines to inspections and agents to showings, you can sell your home today without any hassle. Call us now and we will send a fair cash offer within one business day.</p>
      <h4>If you need to sell a home fast because of :</h4>
      <ul>
        <li><svg width="12" height="12" viewBox="0 0 14 14"><path d="M2 7l3 3 7-7" stroke="#0592cd" stroke-width="2.2" fill="none"/></svg>Divorce or Bankruptcy</li>
        <li><svg width="12" height="12" viewBox="0 0 14 14"><path d="M2 7l3 3 7-7" stroke="#0592cd" stroke-width="2.2" fill="none"/></svg>Foreclosure</li>
        <li><svg width="12" height="12" viewBox="0 0 14 14"><path d="M2 7l3 3 7-7" stroke="#0592cd" stroke-width="2.2" fill="none"/></svg>Landlord problems evictions with tenants okay</li>
        <li><svg width="12" height="12" viewBox="0 0 14 14"><path d="M2 7l3 3 7-7" stroke="#0592cd" stroke-width="2.2" fill="none"/></svg>Inherited property or probate</li>
        <li><svg width="12" height="12" viewBox="0 0 14 14"><path d="M2 7l3 3 7-7" stroke="#0592cd" stroke-width="2.2" fill="none"/></svg>Termites, mold, flood or fire damage, leaky roof</li>
        <li><svg width="12" height="12" viewBox="0 0 14 14"><path d="M2 7l3 3 7-7" stroke="#0592cd" stroke-width="2.2" fill="none"/></svg>Moving or can't afford mortgage payments</li>
      </ul>
      <p style="margin-top:12px">We Can Help.</p>
      <p>We are the Easiest home buyers around.</p>
    </div>

    <div class="sidebar">
      <div class="privacy">
        <h5>OUR PRIVACY POLICY</h5>
        <div class="socials"><span></span><span></span><span></span><span></span></div>
      </div>
      <div class="call-bar">Call Us 8 To 10 Pm Eastern Time. We Answer Our Phones.</div>
      <div class="testimonial">
        <h5>Home Seller Testimonials</h5>
        <p>I just wanted to thank you for buying my home in Harlow Park. You made it fast and easy and kept me well informed the whole way.</p>
        <div class="by"><span>Delia Varnok — Harlow Park</span><span>More Testimonials</span></div>
      </div>
      <div class="about">
        <div class="photo" role="img" aria-label="Portrait photo of the company owner"></div>
        <div>
          <h5>ABOUT US</h5>
          <p>Owned and operated in central Florida since 2003. Over a thousand homes purchased and closed, with local experts in every market we serve.</p>
        </div>
      </div>
    </div>
  </div>
</section>

<section class="lower">
  <div class="wrap">
    <div class="posts">
      <article class="post">
        <div class="thumb" role="img" aria-label="Photo of a family outside a home" style="background:linear-gradient(#8fb4d6,#5f7f52)"></div>
        <div><h6>SEO UT PERSPICIATIS UNDE</h6><p>Sed ut perspiciatis unde omnis iste natus error sit voluptatem accusantium doloremque laudantium, totam rem aperiam eaque ipsa quae ab illo inventore veritatis.</p><p class="meta">Read more</p></div>
      </article>
      <article class="post">
        <div class="thumb" role="img" aria-label="Photo of a couple holding house keys" style="background:linear-gradient(#c9b89a,#7d6a52)"></div>
        <div><h6>SEO UT PERSPICIATIS UNDE</h6><p>Nemo enim ipsam voluptatem quia voluptas sit aspernatur aut odit aut fugit, sed quia consequuntur magni dolores eos qui ratione sequi nesciunt.</p><p class="meta">Read more</p></div>
      </article>
      <article class="post">
        <div class="thumb" role="img" aria-label="Photo of a suburban house front" style="background:linear-gradient(#a8c4e0,#8a9a70)"></div>
        <div><h6>SEO UT PERSPICIATIS UNDE</h6><p>Neque porro quisquam est qui dolorem ipsum quia dolor sit amet, consectetur adipisci velit, sed quia non numquam eius modi tempora incidunt.</p><p class="meta">Read more</p></div>
      </article>
    </div>
    <div class="cities">
      <h4>Some Of The Cities We Buy Houses, Not All Are Listed.</h4>
      <p>There are the cities where we have an affiliate where you can sell a home fast or quickly and we buy homes for cash across the region, from Orlando and Sanford to Kissimmee, Ocala, Tampa, Daytona and many nearby towns.</p>
      <p>These are the types of real estate that we buy: single family homes, town houses, condos, duplexes, mobile homes and vacant land in any condition.</p>
      <div class="pic" role="img" aria-label="Photo of a neighbourhood street with houses"></div>
      <p class="caption">We buy nice pretty houses and some ugly ones as well.</p>
    </div>
  </div>
</section>

<nav class="links">
  <div class="wrap">
    <span>Archives</span><span>We Buy Houses</span><span>Sell Your House</span>
    <span>Sell My House</span><span>Real Estate Investors</span><span>Cash Offer</span>
  </div>
</nav>

<footer class="site-footer">
  <div class="wrap">
    <div class="brand"><span class="mark"></span>quorvadeal.com</div>
    <div class="fcol">
      <h6>Quick Links</h6>
      <ul><li>We Buy Houses</li><li>Sell Home Today Online</li><li>Sell House Fast For Cash</li><li>Cash Home Buyer</li><li>Company</li></ul>
    </div>
    <div class="fcol">
      <h6>Connect With US</h6>
      <p>hello@quorvadeal.com</p>
      <div class="socials" style="margin-top:8px"><span></span><span></span><span></span><span></span><span></span></div>
    </div>
    <div class="fcol">
      <h6>Contact Us</h6>
      <p>2140 Marrowind Ave #300<br>Harlow Park, FL 32700</p>
      <p style="margin-top:8px">TOLL FREE : 1-888-555-0142</p>
      <p>hello@quorvadeal.com</p>
    </div>
  </div>
</footer>
<div class="bottom"><div class="wrap">© 2014 All Rights Reserved. quorvadeal.com</div></div>

</body>
</html>
```